professional business card

Professional business card with logo on one side, and underneath logo list:
- power
-data
-fibre optic
-isolar

On other side:
Marcus Webb
Owner
MOB 0432 958 720
marcus@vorn.com.au
www.vornelectrical.com.au

Please edit logo to just leave VORN

```html
<!DOCTYPE html>
<html lang="en">
<head>
<meta charset="utf-8">
<title>VORN – Business Card</title>
<link rel="stylesheet" href="https://fonts.googleapis.com/css2?family=Open+Sans:wght@400;600;700&display=swap">
<style>
  :root {
    --backdrop: #2b2f33;
    --card: #f7f7f5;
    --teal: #1f8a8c;
    --grey-text: #5f6163;
    --dark-text: #3a3c3e;
    --rule: #7b7d80;
  }
  * { margin: 0; padding: 0; box-sizing: border-box; }
  html, body {
    width: 1200px;
    height: 802px;
    overflow: hidden;
    background: var(--backdrop);
    font-family: "Open Sans", Arial, sans-serif;
  }
  .canvas {
    width: 1200px;
    height: 802px;
    display: flex;
    align-items: center;
    justify-content: center;
  }
  .business-card {
    position: relative;
    width: 1000px;
    height: 572px;
    background: var(--card);
    box-shadow: 0 18px 40px rgba(0,0,0,0.35);
  }
  .brand {
    position: absolute;
    left: 150px;
    top: 62px;
    width: 560px;
  }
  .brand-name {
    font-weight: 700;
    font-size: 128px;
    line-height: 1;
    letter-spacing: 4px;
    color: var(--teal);
  }
  .brand-rule {
    height: 2px;
    background: var(--rule);
    margin-top: 4px;
  }
  .service-list {
    list-style: none;
    display: flex;
    justify-content: space-between;
    margin-top: 12px;
    font-size: 22px;
    letter-spacing: 5px;
    color: var(--grey-text);
    line-height: 1;
  }
  .service-item:not(:last-child)::after {
    content: "\00B7";
    margin-left: 14px;
    color: var(--teal);
  }
  .brand-licence {
    margin-top: 14px;
    font-size: 20px;
    letter-spacing: 12px;
    color: var(--grey-text);
    line-height: 1;
  }
  .contact-block {
    position: absolute;
    left: 150px;
    top: 318px;
  }
  .person-name {
    font-weight: 700;
    font-size: 30px;
    color: var(--teal);
    line-height: 1.1;
  }
  .person-role {
    font-size: 20px;
    color: var(--grey-text);
    margin-bottom: 26px;
  }
  .contact-list { list-style: none; }
  .contact-item {
    display: flex;
    align-items: center;
    gap: 12px;
    font-size: 24px;
    color: var(--dark-text);
    line-height: 1.45;
  }
  .contact-icon { width: 20px; height: 20px; flex: none; }
</style>
</head>
<body>
<main class="canvas">
  <section class="business-card" aria-label="VORN business card">
    <header class="brand">
      <div class="brand-name">VORN</div>
      <div class="brand-rule"></div>
      <ul class="service-list">
        <li class="service-item">POWER</li>
        <li class="service-item">DATA</li>
        <li class="service-item">FIBRE OPTIC</li>
        <li class="service-item">SOLAR</li>
      </ul>
      <div class="brand-licence">EC20587</div>
    </header>

    <div class="contact-block">
      <p class="person-name">Marcus Webb</p>
      <p class="person-role">Owner</p>
      <ul class="contact-list">
        <li class="contact-item">
          <svg class="contact-icon" viewBox="0 0 20 20" aria-hidden="true">
            <rect x="5" y="1" width="10" height="18" rx="2" fill="none" stroke="#1f8a8c" stroke-width="2"/>
            <circle cx="10" cy="15.5" r="1.2" fill="#1f8a8c"/>
          </svg>
          0432 958 720
        </li>
        <li class="contact-item">
          <svg class="contact-icon" viewBox="0 0 20 20" aria-hidden="true">
            <rect x="1" y="4" width="18" height="12" rx="1" fill="#1f8a8c"/>
            <path d="M1 4.5 L10 11 L19 4.5" fill="none" stroke="#f7f7f5" stroke-width="1.6"/>
          </svg>
          marcus@vorn.com.au
        </li>
        <li class="contact-item">
          <svg class="contact-icon" viewBox="0 0 20 20" aria-hidden="true">
            <circle cx="10" cy="10" r="9" fill="#1f8a8c"/>
            <path d="M3 10 H17 M10 1.5 C6 6 6 14 10 18.5 M10 1.5 C14 6 14 14 10 18.5" fill="none" stroke="#f7f7f5" stroke-width="1.3"/>
          </svg>
          www.vornelectrical.com.au
        </li>
      </ul>
    </div>
  </section>
</main>
</body>
</html>
```